Label Design for a New Alcoholized Root Beer

Create a design for a new alcoholized root beer. This is a new product category in the USA growing very rapidly. Root Beer is a popular flavor of Cola, but recently, beer manufacturers have added alcohol to it and have created a new product that has gained traction on the market at a tremendous rate.

Root Beer is vintage product that has been around for a hundred years. Consumers of this product are mostly male between the age of 30 to 45. They purchase this product for its nostalgia and vintage look and taste.

This product will be in a standard 355 mL brown bottle.

It is 5.9% abv.

The name of the product is ''Corvel's Hard Root Beer''.

We have uploaded some pictures of traditional root beers to give you an idea of the feel we want our product to have and also, the bottle the product will be filled in.

Target Market(s)

Consumers are male 30-45, same market as craft beer consumers

Industry/Entity Type

Product

Requirements
Must have
• Design must have a vintage feel to it

```html
<!DOCTYPE html>
<html lang="en">
<head>
<meta charset="utf-8">
<title>Corvel's Hard Root Beer – Label</title>
<link href="https://fonts.googleapis.com/css2?family=Passion+One:wght@700&family=Yellowtail&family=Alfa+Slab+One&display=swap" rel="stylesheet">
<style>
  :root {
    --label-red: #b02a1e;
    --cream: #fbf7c2;
    --shadow-brown: #5a1410;
  }
  html, body {
    margin: 0;
    padding: 0;
    width: 960px;
    height: 1200px;
    overflow: hidden;
    background: var(--label-red);
  }
  .label {
    width: 960px;
    height: 1200px;
    display: flex;
    flex-direction: column;
    align-items: center;
    justify-content: center;
    color: var(--cream);
    text-align: center;
  }
  .crest {
    display: flex;
    align-items: flex-end;
    gap: 40px;
    margin-bottom: 34px;
  }
  .crest-side {
    display: flex;
    flex-direction: column;
    align-items: center;
    gap: 12px;
    margin-bottom: 62px;
  }
  .crest-stripes {
    display: flex;
    flex-direction: column;
    gap: 7px;
  }
  .crest-stripes span {
    display: block;
    width: 118px;
    height: 9px;
    background: var(--cream);
    box-shadow: 0 3px 0 var(--shadow-brown);
  }
  .mug-art {
    width: 240px;
    height: 270px;
    border-radius: 30px 30px 40px 40px;
    background: linear-gradient(160deg, var(--cream) 0%, #efe6a8 100%);
    opacity: 0.92;
  }
  .brand-name {
    font-family: "Passion One", "Arial Black", sans-serif;
    font-weight: 700;
    font-size: 178px;
    line-height: 0.9;
    letter-spacing: 2px;
    margin: 0;
    color: var(--cream);
  }
  .product-type {
    font-family: "Yellowtail", cursive;
    font-size: 92px;
    line-height: 1;
    margin: 8px 0 34px;
    color: var(--cream);
  }
  .spec {
    font-family: "Alfa Slab One", Georgia, serif;
    font-size: 40px;
    letter-spacing: 1px;
    margin: 0;
    text-shadow: 0 4px 0 var(--shadow-brown);
  }
  .rating {
    display: flex;
    gap: 8px;
    margin: 20px 0 22px;
  }
  .star {
    width: 46px;
    height: 46px;
  }
</style>
</head>
<body>
  <main class="label">
    <div class="crest">
      <div class="crest-side">
        <svg class="star" viewBox="0 0 50 50" aria-hidden="true">
          <polygon points="25,4 31,19 47,19 34,29 39,45 25,35 11,45 16,29 3,19 19,19" fill="none" stroke="#fbf7c2" stroke-width="4" stroke-linejoin="round"/>
        </svg>
        <div class="crest-stripes"><span></span><span></span><span></span></div>
      </div>
      <div class="mug-art" role="img" aria-label="Illustration of a foaming root beer mug"></div>
      <div class="crest-side">
        <svg class="star" viewBox="0 0 50 50" aria-hidden="true">
          <polygon points="25,4 31,19 47,19 34,29 39,45 25,35 11,45 16,29 3,19 19,19" fill="none" stroke="#fbf7c2" stroke-width="4" stroke-linejoin="round"/>
        </svg>
        <div class="crest-stripes"><span></span><span></span><span></span></div>
      </div>
    </div>

    <h1 class="brand-name">CORVEL'S</h1>
    <p class="product-type">Hard Root Beer</p>

    <p class="spec">IT IS 5.9% ABV.</p>
    <div class="rating" aria-hidden="true">
      <svg class="star" viewBox="0 0 50 50"><polygon points="25,4 31,19 47,19 34,29 39,45 25,35 11,45 16,29 3,19 19,19" fill="none" stroke="#fbf7c2" stroke-width="4" stroke-linejoin="round"/></svg>
      <svg class="star" viewBox="0 0 50 50"><polygon points="25,4 31,19 47,19 34,29 39,45 25,35 11,45 16,29 3,19 19,19" fill="none" stroke="#fbf7c2" stroke-width="4" stroke-linejoin="round"/></svg>
      <svg class="star" viewBox="0 0 50 50"><polygon points="25,4 31,19 47,19 34,29 39,45 25,35 11,45 16,29 3,19 19,19" fill="none" stroke="#fbf7c2" stroke-width="4" stroke-linejoin="round"/></svg>
    </div>
    <p class="spec">355 ML.</p>
  </main>
</body>
</html>
```